Halvorn - Refresh the look and feel of an existing website

We currently have an existing website www.halvornworldadvisory.example however it needs a more refreshed 'look and feel'. We are a professional consultancy that works with large corporate organisations and government. Our 'tag line' is A New Way of Thinking. We want the site to communicate "Innovation" and Leading Edge Thinking.

Target Market(s)

Corporate and Professional Clients - Organisation and Business Change

Industry/Entity Type

Management Consulting

Number of Pages Required

1 page

Font styles to use
Sans Serif

Requirements
Must have
• Must have a professional Corporate look and feel. Header 'imagery' is ok but boxes on front page need changing ... along with the words. The focus on home page needs to 'call out' 3 main consulting areas:-
• - Change & Transformation Specialists
• - Innovative Solutions
• - Digital Transformation
• Tag Line for business is ... A New Way of Thinking (Highlighting Halvorn as 'Thought Leaders' in business)
Nice to have
• Less "words' more imagery. Possibly an area for a 'video' or recent articles/blogs on the front page. Needs to have more of an 'interactive' feel. We are open to suggestions.
Should not have
• NA

```html
<!DOCTYPE html>
<html lang="en">
<head>
<meta charset="utf-8">
<title>Halvorn Global Solutions</title>
<link href="https://fonts.googleapis.com/css2?family=Open+Sans:wght@400;600;700&family=Varela+Round&display=swap" rel="stylesheet">
<style>
:root{
  --navy:#2f4a6b;
  --slate:#6f7f98;
  --ink:#3c4450;
  --muted:#6b717a;
  --band:#e4e8f0;
  --news-bg:#e9edf3;
  --teal:#4aa3c4;
  --button:#6c7a94;
  --footer:#222325;
  --footer-line:#7d8aa6;
  --footer-link:#7c8aa8;
  --white:#ffffff;
  --copy-bar:#141415;
}
*{margin:0;padding:0;box-sizing:border-box}
html,body{width:682px;height:1200px;overflow:hidden;background:var(--white)}
body{font-family:"Open Sans",Arial,sans-serif;color:var(--ink);position:relative}

/* header */
.site-header{position:absolute;left:0;top:0;width:682px;height:92px;background:var(--white)}
.brand{position:absolute;left:40px;top:33px;display:flex;align-items:center;gap:8px}
.brand-dot{width:30px;height:30px;border-radius:50%;background:var(--navy)}
.brand-name{font-size:19px;font-weight:600;color:var(--navy);letter-spacing:.5px;line-height:1}
.contact-chip{position:absolute;top:40px;display:flex;gap:9px;align-items:flex-start}
.contact-chip .label{font-size:7px;font-weight:600;color:#9aa0a8;text-transform:uppercase;letter-spacing:.2px}
.contact-chip .value{font-size:9px;font-weight:600;color:var(--muted);margin-top:1px}
.chip-phone{left:335px}
.chip-mail{left:468px}

/* nav */
.main-nav{position:absolute;left:0;top:92px;width:682px;height:32px;background:var(--band)}
.main-nav ul{list-style:none;display:flex;position:absolute;left:39px;top:10px}
.main-nav li{font-size:9px;font-weight:600;color:var(--ink);margin-right:22px}
.search{position:absolute;left:520px;top:6px;width:123px;height:20px;border:1px solid #aab3c2;border-radius:3px;font-size:8px;color:#c3c9d3;text-align:right;padding:4px 12px;background:#eef1f6}

/* hero */
.hero{position:absolute;left:0;top:124px;width:682px;height:295px}
.hero-photo{position:absolute;top:0;left:0;width:682px;height:295px;background:linear-gradient(100deg,#3d6a55 0%,#6e8a86 30%,#a8b4be 55%,#7f8b96 75%,#5a6570 100%)}
.hero-title{position:absolute;left:36px;top:50px;font-family:"Varela Round","Open Sans",sans-serif;font-size:40px;line-height:33px;color:var(--white);font-weight:400}
.hero-sub{position:absolute;left:37px;top:193px;font-size:15px;line-height:20px;color:var(--white);font-weight:600}
.hero-cta{position:absolute;left:33px;top:246px;width:102px;height:27px;background:var(--teal);border-radius:4px;color:var(--white);font-size:12px;text-align:center;line-height:27px}

/* focus areas */
.focus{position:absolute;top:419px;left:0;width:682px;height:215px}
.focus-item{position:absolute;top:44px;width:200px;text-align:center}
.focus-item h3{font-size:9px;font-weight:700;color:var(--ink);letter-spacing:.6px;text-align:center;white-space:nowrap}
.focus-icon{display:block;width:200px;height:34px;margin-top:12px;text-align:center}
.focus-icon svg{display:inline-block}
.focus-item p{display:block;width:172px;margin:9px auto 0;font-size:8px;line-height:13.5px;color:var(--muted);text-align:center;white-space:normal;word-wrap:break-word}
.read-more{display:block;width:200px;margin-top:10px;text-align:center;font-size:8px;font-weight:600;color:var(--navy);white-space:nowrap}
.read-more svg{display:inline-block;vertical-align:middle;margin-left:8px}
.focus-1{left:36px}.focus-2{left:236px}.focus-3{left:451px}

/* news */
.news{position:absolute;top:634px;left:0;width:682px;height:340px;background:var(--news-bg)}
.news-heading{position:absolute;left:38px;top:14px}
.news-heading .kicker{font-size:16px;font-weight:700;color:var(--navy);letter-spacing:1px;line-height:18px}
.news-heading .sub{font-size:16px;color:var(--slate);letter-spacing:.8px;line-height:18px}
.post{position:absolute;top:87px;width:280px;height:240px}
.post-date{position:absolute;left:0;top:36px;width:48px;text-align:right}
.post-date .day{font-size:20px;font-weight:700;color:var(--ink);line-height:22px}
.post-date .month{font-size:9px;color:var(--muted)}
.post-views{position:absolute;left:18px;top:92px;width:30px;text-align:center;font-size:9px;color:var(--muted);line-height:15px}
.post-image{position:absolute;left:61px;top:0;width:210px;height:139px}
.post-excerpt{position:absolute;left:61px;top:155px;width:200px;font-size:8px;line-height:13px;color:var(--ink)}
.view-more{position:absolute;left:61px;top:204px;width:80px;height:28px;background:var(--button);color:var(--white);font-size:8px;text-align:center;line-height:28px}
.post-1{left:52px}.post-2{left:370px}

/* footer */
.site-footer{position:absolute;top:962px;left:0;width:682px;height:218px}
.footer-shape{position:absolute;top:0;left:0}
.footer-brand{position:absolute;left:38px;top:103px;display:flex;align-items:center;gap:8px}
.footer-brand .brand-dot{background:var(--white);width:28px;height:28px}
.footer-brand .brand-name{color:var(--white);font-size:17px}
.footer-col{position:absolute;top:44px}
.footer-col h4{font-size:13px;font-weight:400;color:var(--white);line-height:18px;margin-bottom:14px}
.footer-col ul{list-style:none}
.footer-col li{font-size:8px;line-height:12px;color:var(--footer-link);margin-bottom:8.5px;white-space:nowrap}
.col-contact{left:238px}.col-about{left:388px}.col-services{left:520px}
.contact-line{display:flex;gap:10px;font-size:8px;line-height:12.5px;color:#c9ccd2;margin-bottom:5px}
.contact-line svg{flex:none;margin-top:2px}
.copyright{position:absolute;left:0;top:1180px;width:682px;height:20px;background:var(--copy-bar);color:#b9bcc2;font-size:8px;font-weight:600;text-align:center;line-height:20px}
</style>
</head>
<body>

<header class="site-header">
  <div class="brand"><span class="brand-dot"></span><span class="brand-name">HALVORN</span></div>
  <div class="contact-chip chip-phone">
    <svg width="12" height="22" viewBox="0 0 12 22"><rect x="1" y="1" width="10" height="20" rx="2" fill="none" stroke="#8a9099" stroke-width="1.4"/><circle cx="6" cy="17.5" r="1" fill="#8a9099"/></svg>
    <div><div class="label">Call us today</div><div class="value">(+613) 5550 1482</div></div>
  </div>
  <div class="contact-chip chip-mail">
    <svg width="24" height="20" viewBox="0 0 24 20"><path d="M2 7 L12 1 L22 7 V19 H2 Z M2 7 L12 13 L22 7 M2 19 L9 11 M22 19 L15 11" fill="none" stroke="#8a9099" stroke-width="1.4"/></svg>
    <div><div class="label">Mail us today</div><div class="value">info@halvornworldadvisory.example</div></div>
  </div>
</header>

<nav class="main-nav">
  <ul><li>Home</li><li>About Us</li><li>Our Services</li><li>Solutions</li><li>What's Happening</li><li>Contact Us</li></ul>
  <div class="search">Search</div>
</nav>

<section class="hero">
  <div class="hero-photo" role="img" aria-label="Aerial photograph of a city centre with high-rise towers beside a green park"></div>
  <h1 class="hero-title">Specialists in<br>transformational<br>change and<br>sustainable solutions.</h1>
  <p class="hero-sub">To succeed in a complex world,<br>you need a new way of thinking.</p>
  <div class="hero-cta">LEARN MORE</div>
</section>

<section class="focus">
  <div class="focus-item focus-1">
    <h3>TRANSFORMATION SPECIALISTS</h3>
    <div class="focus-icon"><svg width="46" height="34" viewBox="0 0 46 34"><rect x="1" y="4" width="44" height="30" rx="2" fill="#f1f1f1"/><rect x="13" y="11" width="20" height="15" fill="none" stroke="#6b717a" stroke-width="1.4"/><rect x="16" y="14" width="14" height="9" fill="none" stroke="#6b717a" stroke-width="1"/></svg></div>
    <p>Nulla ut semper augue, eget euismod quam. Quisque vel ligula nunc. Suspend-isse eleifend massa molestie</p>
    <div class="read-more">Read More<svg width="18" height="6" viewBox="0 0 18 6"><path d="M0 3H16M13 0.5L17 3L13 5.5" fill="none" stroke="#2f4a6b" stroke-width="1"/></svg></div>
  </div>
  <div class="focus-item focus-2">
    <h3>INNOVATIVE SOLUTIONS</h3>
    <div class="focus-icon"><svg width="34" height="34" viewBox="0 0 34 34"><path d="M17 8a7 7 0 0 0-4 12.8V24h8v-3.2A7 7 0 0 0 17 8Z M14 27h6 M15 30h4" fill="none" stroke="#555b63" stroke-width="1.3"/><path d="M17 2v3M6 7l2 2M28 7l-2 2M3 16h3M31 16h-3" stroke="#555b63" stroke-width="1.2"/></svg></div>
    <p>Nulla ut semper augue, eget euismod quam. Quisque vel ligula nunc. Suspend-isse eleifend massa molestie</p>
    <div class="read-more">Read More<svg width="18" height="6" viewBox="0 0 18 6"><path d="M0 3H16M13 0.5L17 3L13 5.5" fill="none" stroke="#2f4a6b" stroke-width="1"/></svg></div>
  </div>
  <div class="focus-item focus-3">
    <h3>DIGITAL TRANSFORMATION</h3>
    <div class="focus-icon"><svg width="34" height="34" viewBox="0 0 34 34"><circle cx="15" cy="11" r="7" fill="none" stroke="#7a8088" stroke-width="1.3"/><rect x="13" y="8" width="4" height="16" rx="2" fill="#6b717a"/><path d="M13 18h10a3 3 0 0 1 3 3v6a5 5 0 0 1-5 5h-4l-6-8z" fill="#6b717a"/></svg></div>
    <p>Nulla ut semper augue, eget euismod quam. Quisque vel ligula nunc. Suspend-isse eleifend massa molestie</p>
    <div class="read-more">Read More<svg width="18" height="6" viewBox="0 0 18 6"><path d="M0 3H16M13 0.5L17 3L13 5.5" fill="none" stroke="#2f4a6b" stroke-width="1"/></svg></div>
  </div>
</section>

<section class="news">
  <div class="news-heading"><div class="kicker">NEWS</div><div class="sub">From Our Blog</div></div>

  <article class="post post-1">
    <div class="post-date"><div class="day">26</div><div class="month">Nov-2015</div></div>
    <div class="post-views"><svg width="20" height="12" viewBox="0 0 20 12"><path d="M1 6C4 1.5 16 1.5 19 6C16 10.5 4 10.5 1 6Z" fill="none" stroke="#222" stroke-width="1.4"/><circle cx="10" cy="6" r="2.6" fill="none" stroke="#222" stroke-width="1.4"/></svg><br>357 -<br>Views</div>
    <div class="post-image" role="img" aria-label="Business meeting with a tablet showing charts and a cup of coffee" style="background:linear-gradient(135deg,#c9d3dd,#eef1f4 50%,#9aa8b8)"></div>
    <p class="post-excerpt">Nulla ut semper augue, eget euismod quam. Quisque vel ligula nunc. Suspendisse eleifend massa molestie</p>
    <div class="view-more">View More</div>
  </article>

  <article class="post post-2">
    <div class="post-date"><div class="day">26</div><div class="month">Nov-2015</div></div>
    <div class="post-views"><svg width="20" height="12" viewBox="0 0 20 12"><path d="M1 6C4 1.5 16 1.5 19 6C16 10.5 4 10.5 1 6Z" fill="none" stroke="#222" stroke-width="1.4"/><circle cx="10" cy="6" r="2.6" fill="none" stroke="#222" stroke-width="1.4"/></svg><br>357 -<br>Views</div>
    <div class="post-image" role="img" aria-label="Businessman touching a glowing digital interface" style="background:radial-gradient(circle at 55% 45%,#8fb4d6,#3c5f86 55%,#1f3350)"></div>
    <p class="post-excerpt">Nulla ut semper augue, eget euismod quam. Quisque vel ligula nunc. Suspendisse eleifend massa molestie</p>
    <div class="view-more">View More</div>
  </article>
</section>

<footer class="site-footer">
  <svg class="footer-shape" width="682" height="218" viewBox="0 0 682 218">
    <path d="M0 0 L88 6 Q380 12 682 10 V218 H0 Z" fill="var(--footer)"/>
    <path d="M0 0 L88 6 Q380 12 682 10" fill="none" stroke="var(--footer-line)" stroke-width="3"/>
    <path d="M164 7 V66 L215 113 L164 160 V198 H88 L80 218" fill="none" stroke="var(--footer-line)" stroke-width="3"/>
  </svg>
  <div class="footer-brand"><span class="brand-dot"></span><span class="brand-name">HALVORN</span></div>

  <div class="footer-col col-contact">
    <h4>Contact Info</h4>
    <div class="contact-line"><svg width="6" height="8" viewBox="0 0 6 8"><path d="M3 8C0 4 0 3 0 3a3 3 0 0 1 6 0s0 1-3 5Z" fill="#8a8f98"/></svg><span>PO Box 418<br>Harbour Lane East<br>Victoria 8012<br>AUSTRALIA</span></div>
    <div class="contact-line" style="margin-top:10px"><svg width="7" height="7" viewBox="0 0 7 7"><path d="M1 0L2.5 0 3 2 2 3C2.6 4.2 3.2 4.7 4 5L5 4 7 4.5V6C7 6.6 6.5 7 6 7 3 7 0 4 0 1 0 .5.4 0 1 0Z" fill="#8a8f98"/></svg><span>1300 555 218 (Aus)</span></div>
    <div class="contact-line" style="padding-left:17px">0800 555 218 (NZ)</div>
    <div class="contact-line" style="padding-left:17px">1300 555 219 (Intl)</div>
  </div>

  <div class="footer-col col-about">
    <h4>About Us</h4>
    <ul><li>Our Team</li><li>Our Values</li><li>Giving Back</li></ul>
  </div>

  <div class="footer-col col-services">
    <h4>Our Services</h4>
    <ul><li>Strategy and Design</li><li>Transformation</li><li>Change &amp; Culture</li><li>Organisational Development</li><li>Project Management</li><li>Organisational Efficiency</li><li>Specialist Placements</li></ul>
  </div>
</footer>

<div class="copyright">Copyright © 2016 Halvorn Global Solutions</div>

</body>
</html>
```